Tarjetas de visita para empresa de aluminio

Empresa con mas de 40 años vendiendo perfiles de aluminio.
Somos fábrica y almacén, queremos renovar la tarjeta de presentación de nuestros comerciales dando una imgen innovadora y tecnógica mezclado con la calidez del respeto al medio ambiente.
Añado el logo de la empresa y actual cara trasera de la tarjeta de visita, el logo es el simbolo WM y la marca TRAVENIC EXTRUSION, la frase 2extrusion y lacado de aluminio" debe cambiarse por "Diseño, extrusión, lacado, anodizado y mecanizado de precisión de aluminio" o en su defecto incluir todos esos servicios que hacemos o una frase mas pegadiza.

We are an aluminium factory, we produce and stock profiles of aluminium.
we want to renew visit card of our sellers, we are looking for something that show innovation, tecnology and environment respect.
Upload our actual logo and back of visit card, logo WM and brand TRAVENIC EXTRUSION must be keept.
Text "Extrusion y lacado de aluminio" must be changed for "Diseño, extrusion, lacado, anodizado y mecanizado de precisión de aluminio" or something like that

```html
<!DOCTYPE html>
<html lang="es">
<head>
<meta charset="utf-8">
<title>Borrador 1 – Tarjetas Travenic Extrusion</title>
<link href="https://fonts.googleapis.com/css2?family=Josefin+Sans:wght@300;400;600&family=Open+Sans:wght@600;700&family=Tinos:wght@400;700&display=swap" rel="stylesheet">
<style>
:root{
  --sheet:#ffffff;
  --panel:#afb2b7;
  --title:#7a7f97;
  --navy:#03265a;
  --slate:#2e3859;
  --cream:#e5ddcc;
  --silver:#c5c8d2;
  --petrol:#1f384d;
  --ink-warm:#3a3430;
  --ink-navy:#2e3a66;
  --ink-teal:#1f3a4a;
  --silver-text:#d9dde3;
  --white:#ffffff;
}
*{margin:0;padding:0;box-sizing:border-box}
html,body{width:1090px;height:1200px;overflow:hidden;background:var(--sheet)}
.board{position:relative;width:1090px;height:1200px}
.board-title{position:absolute;top:38px;left:0;width:1090px;text-align:center;
  font:300 25px/1 'Josefin Sans',sans-serif;letter-spacing:11px;color:var(--title);padding-left:8px}
.panel{position:absolute;left:41px;width:1007px;background:var(--panel)}
.panel-a{top:105px;height:331px}
.panel-b{top:449px;height:328px}
.panel-c{top:790px;height:358px}
.panel-label{position:absolute;left:22px;top:28px;font:300 24px/1 'Josefin Sans',sans-serif;letter-spacing:9px;color:var(--white)}
.card{position:absolute;top:92px;width:367px;height:210px;box-shadow:4px 6px 10px rgba(0,0,0,.35);overflow:hidden}
.panel-b .card{top:73px}
.panel-c .card{top:73px}
.card-front{left:100px}
.card-back{left:531px}

.brand{display:flex;flex-direction:column;align-items:center;text-align:center}
.brand-mark{border-radius:50%;border:3px solid currentColor}
.brand-name{font-family:'Josefin Sans',sans-serif;font-weight:600;letter-spacing:1.5px}
.brand-tagline{font-family:'Josefin Sans',sans-serif;font-weight:400;line-height:1.35;letter-spacing:.2px}

.front-a{background:var(--navy);color:var(--silver-text)}
.front-a .brand{margin-top:48px}
.front-a .brand-mark{width:56px;height:56px}
.front-a .brand-name{font-size:19px;margin-top:14px}
.front-a .brand-tagline{font-size:8px;margin-top:9px}

.front-b{background:var(--slate);color:var(--silver-text)}
.front-b .brand{margin-top:52px}
.front-b .brand-mark{width:48px;height:48px}
.front-b .brand-name{font-size:15px;margin-top:12px}
.front-b .brand-tagline{font-size:9.5px;margin-top:18px;color:var(--white)}

.front-c{background:var(--white);color:var(--petrol)}
.front-c .brand{margin-top:40px}
.front-c .brand-mark{width:70px;height:70px;border-width:5px;border-color:#4c7495}
.front-c .brand-name{font-size:22px;margin-top:12px;color:#1a2430}
.front-c .brand-tagline{font-size:8px;margin-top:16px}

.back-a{background:var(--cream);color:var(--ink-warm)}
.back-b{background:var(--silver);color:var(--ink-navy)}
.back-c{background:var(--petrol);color:var(--white)}

.mini-brand{position:absolute;display:flex;flex-direction:column;align-items:center;text-align:center;color:var(--ink-warm)}
.mini-brand .brand-mark{border-width:2px}
.back-a .mini-brand{left:14px;top:16px;width:118px}
.back-a .brand-mark{width:26px;height:26px}
.back-a .brand-name{font-size:9px;margin-top:5px;letter-spacing:.5px}
.back-a .brand-tagline{font-size:3.6px;margin-top:3px}
.back-b .mini-brand{left:133px;top:20px;width:100px;color:var(--ink-navy)}
.back-b .brand-mark{width:20px;height:20px}
.back-b .brand-name{font-size:7px;margin-top:3px;letter-spacing:.5px}
.back-b .brand-tagline{font-size:3px;margin-top:2px}

.holder{position:absolute;left:0;width:100%;text-align:center}
.holder-name{font-family:'Tinos',serif;font-weight:700}
.holder-role{font-family:'Tinos',serif;font-weight:400}
.back-a .holder{top:88px}
.back-a .holder-name{font-size:14px;letter-spacing:.3px}
.back-a .holder-role{font-size:13px;margin-top:3px}
.back-b .holder{top:74px}
.back-b .holder-name{font-size:19px}
.back-b .holder-role{font-size:15px;margin-top:1px}

.contact{position:absolute;font:700 8.6px/9.4px 'Open Sans',sans-serif}
.contact-left{left:15px;text-align:left}
.contact-right{right:15px;text-align:right}
.back-a .contact{top:163px}
.back-b .contact-left{left:14px;top:163px}
.back-b .contact-right{right:12px;top:161px;color:var(--ink-teal)}
.back-a .contact-right{color:#2a2a2a}

.back-c .holder{top:27px}
.back-c .holder-name{font-family:'Open Sans',sans-serif;font-weight:700;font-size:20px;letter-spacing:.3px}
.back-c .holder-role{font-family:'Open Sans',sans-serif;font-weight:700;font-size:9.5px;margin-top:4px}
.back-c .holder-email{position:absolute;top:121px;left:0;width:100%;text-align:center;font:600 16px/1 'Open Sans',sans-serif}
.back-c .contact{font-size:6.6px;line-height:6.8px;top:175px}
.back-c .contact-left{left:13px}
.back-c .contact-right{right:8px;font-size:7.6px;line-height:9.4px;top:174px}
</style>
</head>
<body>
<main class="board">
  <h1 class="board-title">BORRADOR 1</h1>

  <section class="panel panel-a">
    <h2 class="panel-label">DISEÑO A</h2>
    <article class="card card-front front-a">
      <div class="brand">
        <span class="brand-mark"></span>
        <span class="brand-name">TRAVENIC EXTRUSION</span>
        <p class="brand-tagline">DISEÑO, EXTRUSIÓN, LACADO, ADONIZADO Y MECANIZADO<br>DE PRECISIÓN DE ALUMINIO</p>
      </div>
    </article>
    <article class="card card-back back-a">
      <div class="mini-brand">
        <span class="brand-mark"></span>
        <span class="brand-name">TRAVENIC EXTRUSION</span>
        <p class="brand-tagline">DISEÑO, EXTRUSIÓN, LACADO, ADONIZADO Y MECANIZADO<br>DE PRECISIÓN DE ALUMINIO</p>
      </div>
      <div class="holder">
        <p class="holder-name">MARCOS RIVERA SOLER</p>
        <p class="holder-role">Comercial</p>
      </div>
      <p class="contact contact-left">Pol. Ind. Las Lomas - C/4 N 12<br>41720 Villaverde del Campo (Sevilla)<br>Apartado de Correos 245<br>Email: marcosrivera@travenic.com</p>
      <p class="contact contact-right">Móvil: 600 12 34 56<br>Telf: 955 00 11 22<br>Fax: 955 00 33 44<br>www.travenic.com</p>
    </article>
  </section>

  <section class="panel panel-b">
    <h2 class="panel-label">DISEÑO B</h2>
    <article class="card card-front front-b">
      <div class="brand">
        <span class="brand-mark"></span>
        <span class="brand-name">TRAVENIC EXTRUSION</span>
        <p class="brand-tagline">DISEÑO, EXTRUSIÓN, LACADO, ADONIZADO Y MECANIZADO<br>DE PRECISIÓN DE ALUMINIO</p>
      </div>
    </article>
    <article class="card card-back back-b">
      <div class="mini-brand">
        <span class="brand-mark"></span>
        <span class="brand-name">TRAVENIC EXTRUSION</span>
        <p class="brand-tagline">DISEÑO, EXTRUSIÓN, LACADO, ADONIZADO Y MECANIZADO<br>DE PRECISIÓN DE ALUMINIO</p>
      </div>
      <div class="holder">
        <p class="holder-name">MARCOS RIVERA SOLER</p>
        <p class="holder-role">Comercial</p>
      </div>
      <p class="contact contact-left">Pol. Ind. Las Lomas - C/4 N 12<br>41720 Villaverde del Campo (Sevilla)<br>Apartado de Correos 245<br>Email: marcosrivera@travenic.com</p>
      <p class="contact contact-right">Móvil: 600 12 34 56<br>Telf: 955 00 11 22<br>Fax: 955 00 33 44<br>www.travenic.com</p>
    </article>
  </section>

  <section class="panel panel-c">
    <h2 class="panel-label">DISEÑO C</h2>
    <article class="card card-front front-c">
      <div class="brand">
        <span class="brand-mark"></span>
        <span class="brand-name">TRAVENIC EXTRUSION</span>
        <p class="brand-tagline">DISEÑO, EXTRUSIÓN, LACADO, ADONIZADO Y MECANIZADO<br>DE PRECISIÓN DE ALUMINIO</p>
      </div>
    </article>
    <article class="card card-back back-c">
      <div class="holder">
        <p class="holder-name">MARCOS RIVERA SOLER</p>
        <p class="holder-role">COMERCIAL</p>
      </div>
      <p class="holder-email">marcosrivera@travenic.com</p>
      <p class="contact contact-left">Pol. Ind. Las Lomas - C/4 N 12<br>41720 Villaverde del Campo (Sevilla)<br>Apartado de Correos 245<br>www.travenic.com</p>
      <p class="contact contact-right">Móvil: 600 12 34 56<br>Telf: 955 00 11 22<br>Fax: 955 00 33 44</p>
    </article>
  </section>
</main>
</body>
</html>
```